Coralbend Pastoral Traders Business Cards

We require business cards revamped with our logo. A few details we would like to use.

1. Round Edges
2. Our logo over the top of a wagyu cattle background photo on one side of the card

Other side of the card has the below details.

1. Person Name (First & Last)
2. Job Position
3. Mobile Number
4. Email Address
5. Website Address

Simple & Neat.

Target Market(s)

Sales

Industry/Entity Type

Agriculture

Contact Information for Business Card

CORALBEND PASTORAL TRADERS

Colors

Designer to choose colors to be used in the design.

Requirements
Must have
• Company Logo

```html
<!DOCTYPE html>
<html lang="en">
<head>
<meta charset="utf-8">
<title>Coralbend Pastoral Traders – Business Cards</title>
<link href="https://fonts.googleapis.com/css2?family=Lato:wght@300;400;700;900&display=swap" rel="stylesheet">
<style>
  :root {
    --stage: #2b2d31;
    --card: #5e0d25;
    --card-deep: #520a1f;
    --ink: #ffffff;
    --ink-soft: rgba(255,255,255,0.88);
  }
  * { margin: 0; padding: 0; box-sizing: border-box; }
  html, body { width: 1200px; height: 952px; overflow: hidden; }
  body {
    background: var(--stage);
    font-family: "Lato", Arial, sans-serif;
    position: relative;
  }
  .card {
    position: absolute;
    width: 560px;
    height: 320px;
    background: var(--card);
    border-radius: 16px;
    overflow: hidden;
    box-shadow: 0 14px 30px rgba(0,0,0,0.45);
  }
  .card--front { left: 70px; top: 520px; }
  .card--back { left: 570px; top: 110px; }

  .brand {
    position: absolute;
    inset: 0;
    display: flex;
    align-items: center;
    justify-content: center;
    gap: 14px;
  }
  .brand__dot {
    width: 34px; height: 34px;
    border-radius: 50%;
    background: var(--ink);
  }
  .brand__name {
    color: var(--ink);
    font-weight: 900;
    font-size: 27px;
    letter-spacing: 0.5px;
  }

  .watermark {
    position: absolute;
    right: 90px; bottom: -50px;
    width: 270px; height: 270px;
    border-radius: 50%;
    background: var(--card-deep);
  }

  .holder { position: absolute; left: 44px; top: 42px; }
  .holder__name {
    color: var(--ink);
    font-size: 21px;
    letter-spacing: 0.6px;
    font-weight: 400;
  }
  .holder__name b { font-weight: 900; }
  .holder__role {
    color: var(--ink-soft);
    font-size: 14px;
    font-weight: 300;
    margin-top: 2px;
  }

  .contacts {
    position: absolute;
    left: 44px; top: 140px;
    list-style: none;
  }
  .contacts li {
    display: flex;
    align-items: flex-start;
    gap: 10px;
    color: var(--ink);
    font-size: 13px;
    line-height: 1.35;
    margin-bottom: 9px;
  }
  .contacts svg { flex: none; width: 16px; height: 16px; margin-top: 1px; }
</style>
</head>
<body>

  <section class="card card--back" aria-label="Business card, contact side">
    <div class="watermark" aria-hidden="true"></div>
    <div class="holder">
      <h1 class="holder__name">DERMOT A. <b>HALLORAN</b></h1>
      <p class="holder__role">Managing Director</p>
    </div>
    <ul class="contacts">
      <li>
        <svg viewBox="0 0 16 16"><rect width="16" height="16" rx="3" fill="#fff"/><path d="M8 3a3.2 3.2 0 0 0-3.2 3.2C4.8 8.6 8 13 8 13s3.2-4.4 3.2-6.8A3.2 3.2 0 0 0 8 3zm0 4.4a1.2 1.2 0 1 1 0-2.4 1.2 1.2 0 0 1 0 2.4z" fill="#5e0d25"/></svg>
        <span>212 Saltbush Road<br>Emerald, QLD 4720</span>
      </li>
      <li>
        <svg viewBox="0 0 16 16"><rect width="16" height="16" rx="3" fill="#fff"/><path d="M5.2 3.5l1.6 2.3-1 1.1a6.5 6.5 0 0 0 3.3 3.3l1.1-1 2.3 1.6-.8 1.7C7.8 12.3 3.7 8.2 3.5 4.3z" fill="#5e0d25"/></svg>
        <span>+61 407 318 552</span>
      </li>
      <li>
        <svg viewBox="0 0 16 16"><rect width="16" height="16" rx="3" fill="#fff"/><path d="M3.5 5h9v6.5h-9zm0 0L8 8.6 12.5 5" fill="none" stroke="#5e0d25" stroke-width="1.3"/></svg>
        <span>dermot@coralbendtraders.com</span>
      </li>
      <li>
        <svg viewBox="0 0 16 16"><rect width="16" height="16" rx="3" fill="#fff"/><circle cx="8" cy="8" r="4.4" fill="none" stroke="#5e0d25" stroke-width="1.2"/><path d="M3.6 8h8.8M8 3.6c-2 2.4-2 6.4 0 8.8M8 3.6c2 2.4 2 6.4 0 8.8" fill="none" stroke="#5e0d25" stroke-width="1"/></svg>
        <span>www.coralbendtraders.com</span>
      </li>
    </ul>
  </section>

  <section class="card card--front" aria-label="Business card, brand side">
    <div class="brand">
      <span class="brand__dot" aria-hidden="true"></span>
      <span class="brand__name">Coralbend Pastoral Traders</span>
    </div>
  </section>

</body>
</html>
```